Business Card for: Northbrook Financial Advisory Services Inc.

provide strategic financial advisory services to companies in the areas of corporate finance, mergers and acquisitions, executive coaching and strategic planning

Target Market(s)

Companies, banks, accountants, lawyers

Industry/Entity Type

High end business consulting in corporate finance, mergers and acquisitions, consulting

Contact Information for Business Card

Name of company, Name: xxxxxx xxxxxx , CEO, - phone number: 1-xxx-xxx-xxxx, - email address,

Requirements
Must have
• Must be professional and simple.
Nice to have
• simple, straight graphics, must give the impression that we are trustworthy, professional, competent
Should not have
• loud colors, loud design features

```html
<!DOCTYPE html>
<html lang="en">
<head>
<meta charset="utf-8">
<title>Northbrook Financial Advisory Inc. — Business Card</title>
<link rel="stylesheet" href="https://fonts.googleapis.com/css2?family=Montserrat:wght@400;500;700;800&display=swap">
<style>
  :root {
    --backdrop: #c0b6b7;
    --ink: #1a1a1a;
    --paper: #ffffff;
    --rule: #8a8a8a;
  }
  * { margin: 0; padding: 0; box-sizing: border-box; }
  html, body {
    width: 1200px; height: 1200px; overflow: hidden;
    background: var(--backdrop);
    font-family: "Montserrat", Arial, sans-serif;
  }
  .canvas { position: relative; width: 1200px; height: 1200px; }

  .card {
    position: absolute; left: 219px; width: 762px;
    border-radius: 19px; overflow: hidden;
  }
  .card--front { top: 161px; height: 422px; background: var(--ink); color: var(--paper); }
  .card--back  { top: 619px; height: 419px; background: var(--paper); color: var(--ink); }

  .wordmark {
    position: absolute; left: 0; right: 0;
    display: flex; align-items: center; justify-content: center; gap: 18px;
    font-weight: 800;
  }
  .wordmark__dot {
    width: 92px; height: 92px; border-radius: 50%;
    background: currentColor; flex: none;
  }
  .wordmark__text { display: flex; flex-direction: column; align-items: center; line-height: 1; }
  .wordmark__name { font-size: 50px; letter-spacing: 0.5px; }
  .wordmark__sub  { font-size: 22.5px; margin-top: 10px; letter-spacing: 0.3px; }

  .card--front .wordmark { top: 155px; }
  .card--back .wordmark  { top: 68px; }
  .card--back .wordmark__dot { width: 82px; height: 82px; }
  .card--back .wordmark__name { font-size: 44px; }
  .card--back .wordmark__sub { font-size: 20px; margin-top: 9px; }

  .person {
    position: absolute; right: calc(762px - 342px); top: 228px;
    text-align: right;
  }
  .person__name { font-size: 27px; font-weight: 800; letter-spacing: 1.2px; line-height: 1; }
  .person__role { font-size: 16px; font-weight: 500; margin-top: 16px; }

  .divider {
    position: absolute; left: 368px; top: 210px;
    width: 1px; height: 103px; background: var(--rule);
  }

  .contacts { position: absolute; left: 390px; top: 221px; list-style: none; }
  .contacts__item {
    display: flex; align-items: center; gap: 6px;
    height: 29.5px; font-size: 17.5px; font-weight: 500;
  }
  .contacts__icon { width: 18px; height: 18px; flex: none; fill: var(--ink); }

  .address {
    position: absolute; left: 0; right: 0; top: 356px;
    text-align: center; font-size: 16.5px; font-weight: 500;
  }
</style>
</head>
<body>
<main class="canvas">
  <section class="card card--front" aria-label="Card front">
    <div class="wordmark">
      <span class="wordmark__dot"></span>
      <div class="wordmark__text">
        <span class="wordmark__name">NORTHBROOK</span>
        <span class="wordmark__sub">FINANCIAL ADVISORY INC.</span>
      </div>
    </div>
  </section>

  <section class="card card--back" aria-label="Card back">
    <div class="wordmark">
      <span class="wordmark__dot"></span>
      <div class="wordmark__text">
        <span class="wordmark__name">NORTHBROOK</span>
        <span class="wordmark__sub">FINANCIAL ADVISORY INC.</span>
      </div>
    </div>

    <div class="person">
      <p class="person__name">MARCUS ELLERY</p>
      <p class="person__role">Founder &amp; CEO</p>
    </div>

    <div class="divider"></div>

    <ul class="contacts">
      <li class="contacts__item">
        <svg class="contacts__icon" viewBox="0 0 24 24" aria-hidden="true"><path d="M6.6 10.8a15.1 15.1 0 0 0 6.6 6.6l2.2-2.2a1 1 0 0 1 1-.25 11.4 11.4 0 0 0 3.6.57 1 1 0 0 1 1 1V20a1 1 0 0 1-1 1A17 17 0 0 1 3 4a1 1 0 0 1 1-1h3.5a1 1 0 0 1 1 1c0 1.25.2 2.45.57 3.57a1 1 0 0 1-.25 1z"/></svg>
        <span>+33 6 41 58 72 90</span>
      </li>
      <li class="contacts__item">
        <svg class="contacts__icon" viewBox="0 0 24 24" aria-hidden="true"><path d="M2 5h20v14H2z M3.5 6.5 12 13l8.5-6.5" fill="var(--ink)"/><path d="M3.5 6.5 12 13l8.5-6.5" fill="none" stroke="#fff" stroke-width="1.6"/></svg>
        <span>info@northbrookfinancialinc.com</span>
      </li>
      <li class="contacts__item">
        <svg class="contacts__icon" viewBox="0 0 24 24" aria-hidden="true"><circle cx="12" cy="12" r="10"/><path d="M2 12h20M12 2c3 3 3 17 0 20M12 2c-3 3-3 17 0 20" fill="none" stroke="#fff" stroke-width="1.3"/></svg>
        <span>www.northbrookfinancialinc.com</span>
      </li>
    </ul>

    <p class="address">2713 Linden Avenue Washington, DC 20016</p>
  </section>
</main>
</body>
</html>
```